Brimwave.com fiber optic internet website redesign

We need a new website design for our fiber optic internet company that provides internet, phone, and tv services. It should use the text "Tamberlyn fiber optics", and "Shine brighter on Tamberlyn". The design should use the color blue and the attached logo.
We are a 30 year old internet company who started as a dial up internet provider in our basement. Today we design, build, and maintain our own fiber optic internet network to provide service to residential, business, educational, healthcare, and governmental customers

```html
<!DOCTYPE html>
<html lang="en">
<head>
<meta charset="utf-8">
<title>Brimwave.com – Tamberlyn Fiber Optics</title>
<link href="https://fonts.googleapis.com/css2?family=Oswald:wght@400;500;600&family=Inter:wght@400;500;600;700&family=Poppins:wght@400;500&display=swap" rel="stylesheet">
<style>
:root{
  --blue:#1a56a8;
  --blue-dark:#0d3f86;
  --red:#c90a0a;
  --ink:#111;
  --band:#dde9fb;
  --card:#f3f3f3;
  --green:#1a8a3a;
  --foot:#f2f2f2;
}
*{margin:0;padding:0;box-sizing:border-box}
html,body{width:1200px;height:2728px;overflow:hidden;background:#fff;font-family:"Inter",sans-serif;color:var(--ink)}
.page{position:relative;width:1200px;height:2728px}
.abs{position:absolute}

/* header */
.brand{left:60px;top:8px;display:flex;align-items:center;gap:12px}
.brand-dot{width:62px;height:62px;border-radius:50%;background:var(--blue)}
.brand-name{font-family:"Inter",sans-serif;font-weight:600;font-size:30px;color:var(--ink);line-height:1}
.brand-sub{font-size:14px;color:var(--ink);margin-top:2px}
.topbar-phone{left:570px;top:10px;width:215px;height:27px;background:var(--red);clip-path:polygon(4% 0,100% 0,96% 100%,0 100%);color:#fff;font-weight:700;font-size:15px;display:flex;align-items:center;justify-content:center;gap:8px}
.topbar-mail{left:788px;top:10px;width:352px;height:27px;background:var(--blue);clip-path:polygon(2% 0,100% 0,100% 100%,0 100%);border-radius:0 14px 0 0;color:#fff;font-size:11px;display:flex;align-items:center;justify-content:space-around;padding-left:14px}
.topbar-mail span{display:flex;align-items:center;gap:5px}
.nav{left:298px;top:44px;width:842px;height:42px;background:#fff;border-radius:22px 22px 0 0;padding:5px}
.nav ul{list-style:none;display:flex;gap:8px;height:100%;background:#e9eef5;border-radius:18px;padding:4px;justify-content:space-between}
.nav li{flex:1;border-radius:14px;background:#8a9bb6;color:#fff;font-size:13px;display:flex;align-items:center;justify-content:center}

/* hero */
.hero{left:60px;top:80px;width:1080px;height:595px;border-radius:0 0 16px 16px;background:radial-gradient(ellipse at 50% 40%,#4f6f9f 0%,#2b4c7a 45%,#14304f 100%);overflow:hidden}
.hero h1{position:absolute;left:0;right:0;top:210px;text-align:center;font-family:"Oswald",sans-serif;font-weight:500;font-size:82px;letter-spacing:3px;color:#fff}
.hero p{position:absolute;left:200px;right:200px;top:335px;text-align:center;font-size:17px;line-height:30px;color:#fff}
.btn{display:inline-flex;align-items:center;justify-content:center;background:var(--red);color:#fff;font-weight:700;border-radius:30px}
.hero .btn{position:absolute;left:352px;top:440px;width:376px;height:60px;font-size:22px}

/* sections */
.eyebrow{font-size:19px;color:var(--blue);letter-spacing:.3px}
.heading{font-family:"Oswald",sans-serif;font-weight:500;font-size:36px;color:var(--ink)}
.heading em{font-style:normal;color:var(--blue)}
.body{font-size:15px;line-height:22.5px}

.about-img{left:592px;top:740px;width:608px;height:452px;background:linear-gradient(135deg,#f5f5f5 0%,#d9d9d9 50%,#8a8a8a 100%);border-radius:4px}

.band{left:0;top:1192px;width:1200px;height:524px;background:var(--band)}
.feature{background:#e9f1fd;border:1px solid #cfdcef;border-radius:10px;box-shadow:0 2px 6px rgba(0,0,0,.08);padding:18px 12px;text-align:left}
.feature h3{text-align:center;font-size:19px;font-weight:700;margin:6px 0 16px}
.feature .small{font-size:11px;line-height:18.5px}
.feature .icon{display:flex;justify-content:center}

.plan{background:var(--card);border-radius:12px;box-shadow:0 2px 6px rgba(0,0,0,.1);text-align:center;padding:28px 14px 0}
.plan h3{font-size:19px;font-weight:700}
.plan p{font-family:"Poppins",sans-serif;font-size:13.5px;line-height:30px;margin-top:28px;height:150px}
.plan .price{font-size:28px;font-weight:700;margin-top:14px}
.plan .price b{font-size:40px;color:var(--green);font-weight:600}
.plan .btn{width:186px;height:45px;font-size:17px;margin-top:34px}

/* footer */
.footer{left:0;top:2431px;width:1200px;height:297px;background:var(--foot);border-top:1px solid #4a6da6}
.foot-dot{left:60px;top:36px;width:100px;height:100px;border-radius:50%;background:var(--blue)}
.foot-name{left:60px;top:175px;font-family:"Oswald",sans-serif;font-size:19px}
.foot-col h4{font-family:"Oswald",sans-serif;font-weight:400;font-size:18px;margin-bottom:32px}
.foot-col ul{list-style:none;font-size:13px;line-height:26px}
.foot-col li::before{content:"»";margin-right:10px}
.copy{left:60px;top:248px;font-family:"Poppins",sans-serif;font-size:13px}
</style>
</head>
<body>
<div class="page">

  <header>
    <div class="abs brand">
      <div class="brand-dot"></div>
      <div>
        <div class="brand-name">Brimwave.com</div>
        <div class="brand-sub">Tamberlyn Fiber Optics</div>
      </div>
    </div>
    <div class="abs topbar-phone">
      <svg width="15" height="15" viewBox="0 0 24 24" fill="#fff"><path d="M6.6 10.8a15 15 0 006.6 6.6l2.2-2.2c.3-.3.7-.4 1-.2 1.1.4 2.3.6 3.6.6.6 0 1 .4 1 1V20c0 .6-.4 1-1 1A17 17 0 013 4c0-.6.4-1 1-1h3.5c.6 0 1 .4 1 1 0 1.3.2 2.5.6 3.6.1.3 0 .7-.2 1z"/></svg>
      1-888-555-0142
    </div>
    <div class="abs topbar-mail">
      <span><svg width="13" height="13" viewBox="0 0 24 24"><circle cx="12" cy="12" r="11" fill="#fff"/></svg>sales@tamberlyn-mail.com</span>
      <span><svg width="13" height="13" viewBox="0 0 24 24"><circle cx="12" cy="12" r="11" fill="#fff"/><path d="M6 8h12v8H6z" fill="none" stroke="#1a56a8" stroke-width="1.6"/></svg>help@tamberlyn-mail.com</span>
    </div>
    <nav class="abs nav">
      <ul>
        <li>Home</li><li>Residential</li><li>Business</li><li>Services</li><li>FAQ</li><li>Telecom</li><li>Users</li><li>Contact Us</li><li>Support</li>
      </ul>
    </nav>
  </header>

  <section class="abs hero" role="img" aria-label="Night city skyline with glowing network and cloud icons">
    <h1>TAMBERLYN FIBER OPTICS</h1>
    <p>Tamberlyn Fiber Optic Service Offers Low Cost, High Quality, And Extremely Reliable Phone, TV And High-Speed Internet Access.</p>
    <span class="btn">GET IN TOUCH WITH US</span>
  </section>

  <section class="about">
    <div class="abs eyebrow" style="left:60px;top:768px">ABOUT US</div>
    <h2 class="abs heading" style="left:60px;top:800px">Shine Brighter On <em>Tamberlyn</em></h2>
    <p class="abs body" style="left:60px;top:866px;width:535px">Fiber Optic-Based Communications Have Been Used For Years By Government And Industry. But Now Tamberlyn Is Bringing This Leading-Edge Communications Technology To Your Home Or Business.</p>
    <p class="abs body" style="left:60px;top:956px;width:535px">Tamberlyn Outperforms Other Local Internet And Phone Service Providers By Delivering Internet And Phone Service Over The Newest, Most Reliable Communications Network - Fiber Optics!</p>
    <span class="abs btn" style="left:60px;top:1053px;width:225px;height:45px;font-size:17px">LEARN MORE</span>
    <div class="abs about-img" role="img" aria-label="Router, laptop and a hand holding a smartphone on a white desk"></div>
  </section>

  <section class="abs band">
    <div class="abs eyebrow" style="left:60px;top:92px">WHY CHOOSE TAMBERLYN FIBER OPTICS?</div>
    <h2 class="abs heading" style="left:60px;top:124px">Experience The <em>Difference</em></h2>
    <p class="abs body" style="left:60px;top:202px;width:395px">Utilizing Our Own Fiber Optic Network, We Can Bring You Internet Speeds That Far Surpass Traditional DSL Or Cable Services. Internet Service That Is Consistent And Reliable, Combined With Superior Phone Voice Quality, Makes Tamberlyn Fiber Optic The Perfect Choice For Home And Business.</p>
    <span class="abs btn" style="left:60px;top:360px;width:187px;height:45px;font-size:17px">LEARN MORE</span>

    <div class="abs feature" style="left:490px;top:93px;width:316px;height:337px">
      <div class="icon"><svg width="58" height="56" viewBox="0 0 24 24" fill="var(--blue)"><path d="M6.6 10.8a15 15 0 006.6 6.6l2.2-2.2c.3-.3.7-.4 1-.2 1.1.4 2.3.6 3.6.6.6 0 1 .4 1 1V20c0 .6-.4 1-1 1A17 17 0 013 4c0-.6.4-1 1-1h3.5c.6 0 1 .4 1 1 0 1.3.2 2.5.6 3.6.1.3 0 .7-.2 1z"/></svg></div>
      <h3>Local Support</h3>
      <p class="small">Tamberlyn Has Been The Leading Choice For High Quality And Superior Service Since 1995. Tamberlyn Has A Long-Standing Reputation As Having The Best Customer Support In The Industry. We Don't Outsource Our Customer Service Or Technical Support</p>
      <p style="font-weight:700;font-size:16px;margin-top:14px">When You Call, WE Answer!</p>
    </div>
    <div class="abs feature" style="left:823px;top:93px;width:316px;height:337px">
      <div class="icon"><svg width="52" height="56" viewBox="0 0 24 26"><path d="M8 2h8l-2 4h-4z" fill="var(--blue)"/><circle cx="12" cy="16" r="9" fill="var(--blue)"/><text x="12" y="20.5" font-size="12" text-anchor="middle" fill="#fff" font-family="Inter,sans-serif">$</text></svg></div>
      <h3>Save Money</h3>
      <p class="small" style="line-height:15px">By Choosing Tamberlyn Internet AND VoIP Phone Services, You Can Save Money Every Month By Eliminating Your Per Minute Long Distance Rates And Extra Fees For Basic Features. Tamberlyn VoIP Phone Service Includes Unlimited Local And Long Distance Calling Within The Continental United States And Canada As Well As Free Voicemail And Caller ID.</p>
      <p class="small" style="line-height:15px;margin-top:15px">Tamberlyn Gives You Internet And Phone For One Low Rate - On One Bill - With No Installation Fees, Start-Up Fees Or Introductory Rates That Expire And Catch You By Surprise.</p>
    </div>
  </section>

  <section class="pricing">
    <div class="abs eyebrow" style="left:0;width:1200px;text-align:center;top:1808px">OUR PRICING PACKAGES</div>
    <h2 class="abs heading" style="left:0;width:1200px;text-align:center;top:1842px">Choose From Our <em>Packages</em></h2>

    <div class="abs plan" style="left:60px;top:1940px;width:348px;height:398px">
      <h3>High Speed Internet Service</h3>
      <p>Tamberlyn fiber optic service brings the highest quality, fastest, and most reliable internet to your home 25mbps download starting at...</p>
      <div class="price">$<b>55</b>/mo</div>
      <span class="btn">Get Started</span>
    </div>
    <div class="abs plan" style="left:425px;top:1940px;width:348px;height:398px">
      <h3>VoIP Phone Service</h3>
      <p style="font-size:13px;line-height:26.5px">Tamberlyn fiber optic service can save you money every month with reliable phone service. Keep your same number, FREE Voice Mail and Caller ID, truly UNLIMITED local and long distance calling all for one low rate. starting at...</p>
      <div class="price">$<b>25</b>/mo</div>
      <span class="btn">Get Started</span>
    </div>
    <div class="abs plan" style="left:790px;top:1940px;width:349px;height:398px">
      <h3>Phone &amp; Internet Packages</h3>
      <p style="font-size:15.5px">Save even more money by choosing Tamberlyn for both your phone and internet service. Starting at...</p>
      <div class="price">$<b>80</b>/mo</div>
      <span class="btn">Get Started</span>
    </div>
  </section>

  <footer class="abs footer">
    <div class="abs foot-dot"></div>
    <div class="abs foot-name">TAMBERLYN FIBER OPTICS</div>
    <div class="abs foot-col" style="left:507px;top:36px">
      <h4>For Residential:</h4>
      <ul><li>Internet Service</li><li>Phone Service</li><li>Internet &amp; Phone Packages</li></ul>
    </div>
    <div class="abs foot-col" style="left:880px;top:36px">
      <h4>For Business:</h4>
      <ul><li>Internet Service</li><li>Phone Service</li><li>Internet &amp; Phone Packages</li></ul>
    </div>
    <div class="abs copy">© 2024 Tamberlyn Fiber Optics. All Rights Reserved</div>
  </footer>

</div>
</body>
</html>
```